Paws and Meadows is a dog walking service that offers home boarding and pet taxi

I am looking for a eye catching A5 leaflet/flyer design for my dog walking business Paws and Meadows.

The flyer must have my company logo on it (jpeg), a picture of my van (jpeg) and a picture of dogs playing (jpegs 1-5).

The fonts must be easy to read. I am not set on any colour scheme but do like the idea of having a natural background. IE. Green grass and blue sky or some forest setting with green trees. If you don't like this idea or its hard to work with don't worry I am open minded so be creative and do what you thinks best.

I'll provide quick feedback to designs that i like and so we can work together.

The flyers must contain the following:

60 minute group and individual walks
GPS Tracked Walks
Home Boarding
Pet Taxi
Puppy/Pet visits

Offer: 50% off first weeks dogs walks with this flyer.

As well as containing my contact info:

07915382046
www.paws-and-meadows.co.uk
paws-and-meadows@mailbrook.co.uk

Chatterbook, Chirpline and Snapgallery logos must be present as well.

Thanks and Good luck!

Target Market(s)

ANYONE WHO NEEDS THEIR DOG WALKED OR LOOKED AFTER WHEN THEY ARE ON HOLIDAY

Industry/Entity Type

Business

Contact Information for Business Card

THE BUSINESS CARD MUST DISPLAY THE LOGO THAT HAS BEEN UPLOADED IN A FILE. IT MUST LOOK SHARP AND PROFESSIONAL. CONTAIN ALL CONTACT INFO AND HAVE SERVICES OFFERED. SEE PROJECT DESCRIPTION FOR FLYER.

Font styles to use
Serif
Sans Serif

Requirements
Must have
• SEE PROJECT DESCRIPTION
Nice to have
• IT WOULD BE NICE TO HAVE PHOTOS OF MY VAN AND DOGS PLAYING. I HAVE UPLOADED SOME PICS OF VAN TO BE USED AND THERE ARE PICS OF DOGS PLAYING THAT COULD BE USED.

```html
<!DOCTYPE html>
<html lang="en">
<head>
<meta charset="utf-8">
<title>Paws and Meadows – Dog Walking Flyer</title>
<link href="https://fonts.googleapis.com/css2?family=Lato:wght@700;900&family=Roboto+Condensed:wght@400;700&display=swap" rel="stylesheet">
<style>
  :root{
    --page:#e9e6e1;
    --paper:#ffffff;
    --footer:#f1f1f1;
    --green:#1f6b35;
    --green-dark:#17552a;
    --grass:#6db33a;
    --grass-light:#9fd15e;
    --orange:#f6a21b;
    --sky:#cfe6f5;
    --ink:#1d1d1d;
    --link-blue:#1a66b0;
  }
  *{box-sizing:border-box;margin:0;padding:0}
  html,body{width:1200px;height:1200px;overflow:hidden;background:var(--page)}
  .flyer{
    position:absolute;left:177px;top:0;width:920px;height:1305px;
    transform:scale(0.9195);transform-origin:top left;
    background:var(--paper);overflow:hidden;
    font-family:"Lato",sans-serif;color:var(--ink);
  }
  .header{position:absolute;left:0;top:0;width:920px;height:212px;background:linear-gradient(#fff,#f4f4f4)}
  .brand{position:absolute;left:0;right:0;top:126px;display:flex;align-items:center;justify-content:center;gap:14px}
  .brand-dot{width:30px;height:30px;border-radius:50%;background:var(--orange)}
  .brand-name{font-family:"Lato",sans-serif;font-weight:900;font-size:36px;color:var(--ink);letter-spacing:.5px}

  .hero{position:absolute;left:0;top:212px;width:920px;height:533px;
    background:linear-gradient(180deg,#5fa83a 0%,#6cb33f 35%,#7fbd4d 65%,#cfe4bf 90%,#f6faf6 100%)}
  .photo{position:absolute;border-radius:50%;border:6px solid var(--orange);overflow:hidden}
  .photo-dogs-stick{left:40px;top:487px;width:230px;height:230px;background:radial-gradient(circle at 50% 60%,#8a6a3c,#4f7a2a 70%)}
  .photo-van{left:308px;top:448px;width:304px;height:304px;background:radial-gradient(circle at 50% 45%,#68b6e6 0%,#5aa63a 55%,#3d4a3e 100%)}
  .photo-dogs-water{left:655px;top:487px;width:230px;height:230px;background:linear-gradient(180deg,#f2f4f7 0%,#c9d4dc 40%,#4a5660 100%)}

  .services{position:absolute;left:0;top:745px;width:920px;height:275px;
    background:linear-gradient(180deg,#fbfdfe 0%,#e6f1f8 45%,var(--sky) 100%)}
  .service{position:absolute;display:flex;align-items:flex-start;gap:16px}
  .service-icon{flex:0 0 58px;width:58px;height:58px;border-radius:50%;background:var(--green);display:flex;align-items:center;justify-content:center}
  .service-text{font-weight:700;font-size:30px;line-height:42px;color:#222;padding-top:4px}
  .s-walks{left:119px;top:40px}
  .s-gps{left:119px;top:154px}
  .s-home{left:508px;top:33px}
  .s-taxi{left:508px;top:101px}
  .s-visits{left:508px;top:168px}

  .meadow{position:absolute;left:0;top:1020px;width:920px;height:177px;
    background:linear-gradient(180deg,#8cc64a 0%,var(--grass) 40%,#5aa22e 70%,#86c34a 100%)}
  .offer-band{position:absolute;left:0;top:1084px;width:920px;height:84px;background:var(--green)}
  .offer-box{position:absolute;left:48px;top:1065px;width:342px;height:113px;background:var(--orange);
    display:flex;align-items:center;justify-content:center;gap:24px;font-family:"Roboto Condensed",sans-serif;font-weight:700;color:#111}
  .offer-pct{font-size:84px;line-height:1;letter-spacing:-1px}
  .offer-off{font-size:62px;line-height:1;padding-top:14px}
  .offer-text{position:absolute;left:415px;top:1098px;font-family:"Roboto Condensed",sans-serif;font-weight:400;font-size:42px;color:#fff;letter-spacing:.5px}

  .footer{position:absolute;left:0;top:1197px;width:920px;height:108px;background:var(--footer)}
  .contacts{position:absolute;left:0;right:0;top:18px;display:flex;justify-content:center;gap:22px;
    font-family:"Roboto Condensed",sans-serif;font-size:20px;color:#1e1e1e}
  .contact{display:flex;align-items:center;gap:10px}
  .socials{position:absolute;left:0;right:0;top:58px;display:flex;justify-content:center;gap:22px;
    font-family:"Roboto Condensed",sans-serif;font-size:18px;color:#1e1e1e}
  .social{display:flex;align-items:center;gap:7px}
  .social-mark{width:22px;height:22px;border-radius:4px;background:var(--link-blue)}
</style>
</head>
<body>
<main class="flyer">
  <header class="header">
    <div class="brand">
      <span class="brand-dot"></span>
      <span class="brand-name">Paws and Meadows</span>
    </div>
  </header>

  <section class="hero" role="img" aria-label="Photo of many dogs running and playing together on a sunny green field"></section>
  <div class="photo photo-dogs-stick" role="img" aria-label="Photo of two dogs carrying a stick together"></div>
  <div class="photo photo-van" role="img" aria-label="Photo of the rear of the branded dog walking van"></div>
  <div class="photo photo-dogs-water" role="img" aria-label="Photo of dogs splashing through shallow water"></div>

  <section class="services">
    <div class="service s-walks">
      <span class="service-icon"><svg width="34" height="34" viewBox="0 0 34 34" fill="none" stroke="var(--orange)" stroke-width="3" stroke-linecap="round"><path d="M4 22c6-6 12 4 18-2s8-8 8-8"/><circle cx="27" cy="9" r="3"/><path d="M6 28h22"/></svg></span>
      <span class="service-text">60 minute group and<br>individual walks</span>
    </div>
    <div class="service s-gps">
      <span class="service-icon"><svg width="30" height="34" viewBox="0 0 30 34"><path d="M15 2C8 2 3 7 3 13c0 8 12 19 12 19s12-11 12-19C27 7 22 2 15 2z" fill="var(--orange)"/><circle cx="15" cy="13" r="5" fill="var(--green)"/></svg></span>
      <span class="service-text">GPS Tracked Walks</span>
    </div>
    <div class="service s-home">
      <span class="service-icon"><svg width="36" height="34" viewBox="0 0 36 34"><path d="M18 3L3 17h5v14h7v-9h6v9h7V17h5z" fill="var(--orange)"/></svg></span>
      <span class="service-text">Home Boarding</span>
    </div>
    <div class="service s-taxi">
      <span class="service-icon"><svg width="36" height="30" viewBox="0 0 36 30" fill="var(--orange)"><rect x="14" y="1" width="8" height="4" rx="1"/><path d="M9 7h18l4 9H5z"/><rect x="3" y="15" width="30" height="9" rx="3"/><circle cx="10" cy="20" r="2.5" fill="var(--green)"/><circle cx="26" cy="20" r="2.5" fill="var(--green)"/><rect x="5" y="24" width="6" height="4" rx="1"/><rect x="25" y="24" width="6" height="4" rx="1"/></svg></span>
      <span class="service-text">Pet Taxi</span>
    </div>
    <div class="service s-visits">
      <span class="service-icon"><svg width="32" height="32" viewBox="0 0 32 32" fill="var(--orange)"><ellipse cx="16" cy="22" rx="8" ry="7"/><circle cx="7" cy="13" r="3.5"/><circle cx="12.5" cy="7" r="3.5"/><circle cx="19.5" cy="7" r="3.5"/><circle cx="25" cy="13" r="3.5"/></svg></span>
      <span class="service-text">Puppy/Pet visits</span>
    </div>
  </section>

  <section class="meadow" role="img" aria-label="Open green meadow"></section>
  <div class="offer-band"></div>
  <div class="offer-box"><span class="offer-pct">50%</span><span class="offer-off">OFF</span></div>
  <div class="offer-text">FIRST WEEKS DOGS WALKS</div>

  <footer class="footer">
    <div class="contacts">
      <span class="contact"><svg width="24" height="20" viewBox="0 0 24 20" fill="var(--link-blue)"><rect x="1" y="2" width="6" height="16" rx="1"/><rect x="8" y="2" width="15" height="16" rx="1"/><g fill="#fff"><rect x="11" y="5" width="9" height="3"/><rect x="11" y="10" width="2" height="2"/><rect x="14.5" y="10" width="2" height="2"/><rect x="18" y="10" width="2" height="2"/><rect x="11" y="13.5" width="2" height="2"/><rect x="14.5" y="13.5" width="2" height="2"/><rect x="18" y="13.5" width="2" height="2"/></g></svg>07915382046</span>
      <span class="contact"><svg width="22" height="22" viewBox="0 0 22 22" fill="none" stroke="var(--link-blue)" stroke-width="2.2"><circle cx="11" cy="11" r="9"/><path d="M2 11h18M11 2c3 3 3 15 0 18M11 2c-3 3-3 15 0 18"/></svg>www.paws-and-meadows.co.uk</span>
      <span class="contact"><svg width="22" height="16" viewBox="0 0 22 16" fill="none" stroke="var(--link-blue)" stroke-width="2"><rect x="1" y="1" width="20" height="14" rx="1"/><path d="M1 1l10 8 10-8"/></svg>paws-and-meadows@mailbrook.co.uk</span>
    </div>
    <div class="socials">
      <span class="social"><span class="social-mark"></span>Chatterbook</span>
      <span class="social"><span class="social-mark"></span>Chirpline</span>
      <span class="social"><span class="social-mark"></span>Snapgallery</span>
    </div>
  </footer>
</main>
</body>
</html>
```